Letterhead & logo design project

We need a letterhead for a new company called Dornavelle Ltd a firm of Chartered Accountants and Chartered Tax Advisers based in Pangbourne, Berkshire
Updates
Please include the following:
Chartered Accountants and Chartered Tax Advisers
Industry/Entity Type
It Company
Requirements
Must have
- Must have director's name at the bottom of the letterhead. Must also contain some wording at the bottom of the page to be provided by the BQRPT at a later date

```html
<!DOCTYPE html>
<html lang="en">
<head>
<meta charset="UTF-8">
<title>Dornavelle Ltd Letterhead</title>
<link rel="stylesheet" href="https://fonts.googleapis.com/css2?family=Libertinus+Serif:wght@400;600&display=swap">
<style>
  :root {
    --navy: #0b4a78;
    --sky: #4a8ec4;
    --text-blue: #3f78b0;
    --paper: #ffffff;
    --edge: #bdbdbd;
  }
  * { margin: 0; padding: 0; box-sizing: border-box; }
  html, body {
    width: 848px;
    height: 1200px;
    overflow: hidden;
    background: var(--paper);
  }
  .letterhead {
    position: relative;
    width: 848px;
    height: 1200px;
    border: 2px solid var(--edge);
    background: var(--paper);
    font-family: "Libertinus Serif", "Times New Roman", serif;
  }
  .firm-name {
    position: absolute;
    left: 21px;
    top: 18px;
    font-size: 40px;
    font-weight: 400;
    color: var(--sky);
    line-height: 1;
  }
  .firm-tagline {
    position: absolute;
    left: 19px;
    top: 69px;
    width: 558px;
    height: 34px;
    background: var(--navy);
    color: var(--paper);
    font-size: 24px;
    line-height: 34px;
    padding-left: 7px;
    white-space: nowrap;
  }
  .brand-mark {
    position: absolute;
    right: 18px;
    top: 44px;
    display: flex;
    align-items: center;
    gap: 8px;
    color: var(--navy);
    font-size: 22px;
    font-weight: 400;
  }
  .brand-mark .dot {
    width: 30px;
    height: 30px;
    border-radius: 50%;
    background: var(--navy);
  }
  .footer-band {
    position: absolute;
    left: 19px;
    top: 1077px;
    width: 809px;
    height: 37px;
    background: var(--navy);
    border-bottom: 2px solid #9bb6cf;
    color: var(--paper);
    font-size: 22px;
    font-variant: small-caps;
    letter-spacing: 0.5px;
    line-height: 36px;
    text-align: center;
  }
  .footer-contact {
    position: absolute;
    left: 0;
    top: 1118px;
    width: 100%;
    text-align: center;
    color: var(--text-blue);
  }
  .director-name { font-size: 18px; line-height: 24px; }
  .address { font-size: 13.5px; line-height: 20px; }
  .contact-line { font-size: 13.5px; line-height: 20px; }
</style>
</head>
<body>
  <div class="letterhead">
    <header>
      <h1 class="firm-name">Dornavelle Ltd</h1>
      <p class="firm-tagline">Chartered Accountants and Chartered Tax Advisers</p>
      <div class="brand-mark"><span class="dot"></span><span>Dornavelle</span></div>
    </header>
    <footer>
      <p class="footer-band">Providing Solutions For Difficult Circumstances</p>
      <div class="footer-contact">
        <p class="director-name">Director's name</p>
        <p class="address">48 Fernlea Road, 48 Fernlea Road, UK 4410</p>
        <p class="contact-line">Tel.: (44)00-555-0142 | Fax: (44)00-555-0142 | Email: dirname@dnvco.uk</p>
      </div>
    </footer>
  </div>
</body>
</html>
```